Tall Cedar Builders Business Card

I'm looking for a business card design for a start-up Handyman/Construction Company. The organization will double as a ministry to the homeless, hoping to create job opportunity and training to the homeless, providing a pathway back to being "homed". I'm looking for a simple to "seeming" simple design. Open to all thoughts.

Industry/Entity Type

Ministry

Requirements
Must have
• Logo (Attached), Name, Phone, Email and Address. Note - "*Registered and Insured".

```html
<!DOCTYPE html>
<html lang="en">
<head>
<meta charset="utf-8">
<title>Tall Cedar Builders Business Card</title>
<link href="https://fonts.googleapis.com/css2?family=Open+Sans:wght@400;700&display=swap" rel="stylesheet">
<style>
  :root {
    --stage: #000000;
    --card: #eef4e9;
    --navy: #2d3a5b;
    --purple: #6a2c7f;
    --ink: #2a3050;
    --link: #3d3f9e;
  }
  * { margin: 0; padding: 0; box-sizing: border-box; }
  html, body { width: 1200px; height: 403px; overflow: hidden; background: var(--stage); }
  body { position: relative; font-family: "Open Sans", Arial, sans-serif; }

  .card {
    position: absolute;
    top: 75px;
    width: 444px;
    height: 265px;
    background: var(--card);
    overflow: hidden;
  }
  .card--front { left: 147px; }
  .card--back { left: 624px; }

  .card__band {
    position: absolute;
    left: 0; bottom: 0;
    width: 100%;
    height: 29px;
    display: flex;
  }
  .card__band-main { width: 326px; background: var(--navy); }
  .card__band-accent { flex: 1; background: var(--purple); }

  .holder-name {
    position: absolute;
    left: 38px; top: 36px;
    font-size: 15px;
    color: var(--ink);
  }

  .brand-name {
    position: absolute;
    font-weight: 700;
    color: var(--navy);
    white-space: nowrap;
    letter-spacing: 0.2px;
  }
  .card--front .brand-name { left: 226px; top: 45px; font-size: 17px; }
  .card--back .brand-name { left: 0; width: 100%; text-align: center; top: 98px; font-size: 27px; }

  .contact-list {
    position: absolute;
    left: 38px; top: 113px;
    list-style: none;
  }
  .contact-list li {
    display: flex;
    align-items: center;
    height: 18px;
    font-size: 13px;
    color: var(--link);
  }
  .contact-list li::before {
    content: "";
    width: 7px; height: 7px;
    margin-right: 7px;
    background: var(--navy);
  }

  .website {
    position: absolute;
    left: 0; width: 100%;
    top: 154px;
    text-align: center;
    font-size: 20px;
    color: var(--link);
  }
</style>
</head>
<body>
  <section class="card card--front">
    <p class="holder-name">Rafiq Hasan</p>
    <p class="brand-name">Tall Cedar Builders</p>
    <ul class="contact-list">
      <li>01712345670</li>
      <li>rafiqhasan07@mail.com</li>
      <li>Cedar Lane,Dhaka,Bangladesh</li>
      <li>www.tallcedar.com</li>
    </ul>
    <div class="card__band"><span class="card__band-main"></span><span class="card__band-accent"></span></div>
  </section>

  <section class="card card--back">
    <p class="brand-name">Tall Cedar Builders</p>
    <p class="website">www.tallcedar.com</p>
    <div class="card__band"><span class="card__band-main"></span><span class="card__band-accent"></span></div>
  </section>
</body>
</html>
```